Bright Path Therapies business cards and stationary

Need business cards and stationary designed to match previously made logo for for a new company based in Sydney NSW called 'Bright Path Therapies'.

We provide early intervention services and diagnostic assessment for children with disability and their families. I would like designs that are colourful and child friendly - possibly using feet/footprints/steps on a white background. The final design should communicate that we are family friendly, accepting and fun to work with.

Target Market(s)

Parents and Families
Teachers
Allied Health Professionals

Industry/Entity Type

Psychology

Contact Information for Business Card

Bright Path Therapies
www.brightpaththerapies-example.com
info@brightpaththerapies-example.com

Font styles to use
Sans Serif
Decorative
Script

Requirements
Must have
• Match the font and colour scheme of logo, along with footprint picture
Nice to have
• Clean and simple, while reflecting that I am working with families.
• Also- editable for when we make staff specific cards.

```html
<!DOCTYPE html>
<html lang="en">
<head>
<meta charset="UTF-8">
<title>Bright Path Therapies – Business Cards</title>
<link href="https://fonts.googleapis.com/css2?family=Montserrat:wght@400;500;800&display=swap" rel="stylesheet">
<style>
  :root {
    --backdrop: #2b2b2d;
    --card: #ffffff;
    --red: #ee4136;
    --blue: #2a7fc9;
    --text-font: 'Montserrat', sans-serif;
  }
  * { box-sizing: border-box; margin: 0; padding: 0; }
  html, body { width: 1200px; height: 880px; overflow: hidden; }
  body { background: var(--backdrop); font-family: var(--text-font); position: relative; }

  .card {
    position: absolute;
    width: 560px;
    height: 320px;
    background: var(--card);
    box-shadow: 0 14px 30px rgba(0,0,0,.45);
    overflow: hidden;
  }
  .card--front { left: 90px; top: 80px; }
  .card--back  { left: 550px; top: 480px; }

  .brand { display: flex; align-items: center; gap: 12px; }
  .brand__dot { width: 40px; height: 40px; border-radius: 50%; background: var(--red); flex: none; }
  .brand__name { font-weight: 500; color: var(--blue); font-size: 24px; letter-spacing: .5px; }

  .card--front .brand { position: absolute; left: 50%; top: 50%; transform: translate(-50%, -50%); }

  .card--back .brand { position: absolute; right: 34px; top: 46px; }
  .card--back .brand__dot { width: 32px; height: 32px; }
  .card--back .brand__name { font-size: 19px; }

  .feature-art {
    position: absolute; left: 0; top: 110px;
    width: 210px; height: 210px;
    background: var(--red);
    border-top-right-radius: 90px;
  }

  .staff { position: absolute; left: 260px; top: 150px; }
  .staff__name { color: var(--red); font-weight: 800; font-size: 20px; letter-spacing: 1px; text-transform: uppercase; }
  .staff__role { color: var(--blue); font-size: 14px; margin-top: 2px; }

  .contact { position: absolute; left: 260px; top: 222px; list-style: none; }
  .contact__item { display: flex; align-items: center; gap: 8px; color: var(--blue); font-size: 12px; margin-bottom: 6px; }
  .contact__icon { width: 16px; height: 16px; flex: none; }
</style>
</head>
<body>

  <section class="card card--front">
    <div class="brand">
      <span class="brand__dot"></span>
      <span class="brand__name">Bright Path Therapies</span>
    </div>
  </section>

  <section class="card card--back">
    <div class="feature-art" role="img" aria-label="Large decorative area in the brand red, reserved for the brand footprint artwork"></div>

    <div class="brand">
      <span class="brand__dot"></span>
      <span class="brand__name">Bright Path Therapies</span>
    </div>

    <div class="staff">
      <p class="staff__name">Maya Collins</p>
      <p class="staff__role">Manager</p>
    </div>

    <ul class="contact">
      <li class="contact__item">
        <svg class="contact__icon" viewBox="0 0 16 16" fill="none" stroke="#ee4136" stroke-width="1.2">
          <circle cx="8" cy="8" r="7.2"/>
          <path d="M5.2 4.5l1.4 1.4-.8 1c.6 1.2 1.4 2 2.6 2.6l1-.8 1.4 1.4-1 1.2c-2.6-.4-4.6-2.4-5-5z" fill="#ee4136" stroke="none"/>
        </svg>
        <span>(02) 5550 1234</span>
      </li>
      <li class="contact__item">
        <svg class="contact__icon" viewBox="0 0 16 16" fill="none" stroke="#ee4136" stroke-width="1.2">
          <circle cx="8" cy="8" r="7.2"/>
          <rect x="4.3" y="5.3" width="7.4" height="5.4"/>
          <path d="M4.3 5.3L8 8.4l3.7-3.1"/>
        </svg>
        <span>info@brightpaththerapies-example.com</span>
      </li>
      <li class="contact__item">
        <svg class="contact__icon" viewBox="0 0 16 16" fill="none" stroke="#ee4136" stroke-width="1.2">
          <circle cx="8" cy="8" r="7.2"/>
          <circle cx="8" cy="8" r="3.8"/>
          <path d="M4.2 8h7.6M8 4.2c-1.6 2.2-1.6 5.4 0 7.6M8 4.2c1.6 2.2 1.6 5.4 0 7.6"/>
        </svg>
        <span>www.brightpaththerapies-example.com</span>
      </li>
    </ul>
  </section>

</body>
</html>
```